Corlanta yard sign to enhance advertising taking advantage of technology

Yard sign
I have uploaded my Logo and a picture of a home I built
Company Name : CORLANTA
The sign Is 27" x 18"
I want the sign to reflect that perfect day-spring/summer the one that makes you feel good- I want the customer to feel good looking at the sign so it can stay in his yard for a period of time and I want a potential customer to drive by see the sign and think I want my house to look like that. or at least start thinking I should call that company. "that is a real nice sign"

-statement: "Providing the best service to your home so you can live comfortably"
-The house picture I uploaded is optional. I jjust want something that reflects a nice day. Might have to much going on
-Logo with name to the right
-Phone1234567890
-www.Corlanta-example.net
-improve quality, improve value, increase longevity, save thousands (not sure of the best way to word quality, value, longevity and save thousands) if there is a way to sum this up even better. this is optional as well
- everything has to be clear and readable

Potential customers may take pictures of the sign. Is there a way to integrate something to enhance what happens Or at least encourage a potential customer to take pictures and share. Some kind of reaction (may not be possible) if possible let me know
Basically if there is way the yard sign can get more noticed and shared further enhancing its advertising ability. I want to try and take advantage of technology

Target Market(s)

Home owners

Industry/Entity Type

Advertising

Requirements
Must have
• logo & company name CORLANTA
• Providing the best service to your home so you can live comfortably
Nice to have
• i have uploaded an image of a home I built, I like the idea of it being used but if it does not work for what you have imagined don't use it.
• Your ideas.... I know this may seem generic but you guys have amazing talent

```html
<!DOCTYPE html>
<html lang="en">
<head>
<meta charset="utf-8">
<title>Corlanta Yard Sign</title>
<link rel="stylesheet" href="https://fonts.googleapis.com/css2?family=Josefin+Sans:wght@600;700&display=swap">
<style>
  :root {
    --page-bg: #e9ebe6;
    --sign-white: #ffffff;
    --ink-dark: #3a3b3d;
    --band-gray: #55575a;
    --brand-green: #7ac22a;
    --brand-orange: #f07d0c;
    --photo-sky: #9fc3a0;
    --photo-trees: #3f6a3a;
    --photo-house: #d8ccb0;
    --photo-lawn: #6f9440;
  }
  html, body {
    margin: 0;
    width: 1200px;
    height: 927px;
    overflow: hidden;
    background: var(--page-bg);
  }
  .yard-sign {
    position: absolute;
    left: 30px;
    top: 83px;
    width: 1140px;
    height: 760px;
    box-shadow: 0 4px 18px rgba(0,0,0,0.15);
  }
  .sign-text { font-family: "Josefin Sans", "Century Gothic", sans-serif; }
  .tagline { font-size: 14.2px; font-weight: 700; fill: var(--ink-dark); letter-spacing: 0.2px; }
  .brand-name { font-size: 29px; font-weight: 700; fill: var(--ink-dark); letter-spacing: 0.5px; }
  .phone { font-size: 19px; font-weight: 700; fill: var(--ink-dark); }
  .website { font-size: 11.5px; font-weight: 700; fill: var(--ink-dark); letter-spacing: 0.4px; }
  .icon { fill: var(--ink-dark); }
  .icon-stroke { stroke: var(--ink-dark); stroke-width: 1.6; fill: none; }
</style>
</head>
<body>
<svg class="yard-sign" viewBox="0 0 666 444" xmlns="http://www.w3.org/2000/svg" aria-label="Corlanta yard sign">
  <defs>
    <linearGradient id="photo-tones" x1="0" y1="0" x2="0" y2="1">
      <stop offset="0" stop-color="var(--photo-trees)"/>
      <stop offset="0.35" stop-color="var(--photo-sky)"/>
      <stop offset="0.55" stop-color="var(--photo-house)"/>
      <stop offset="0.8" stop-color="var(--photo-house)"/>
      <stop offset="1" stop-color="var(--photo-lawn)"/>
    </linearGradient>
  </defs>

  <rect class="sign-panel" width="666" height="444" fill="var(--sign-white)"/>

  <!-- header -->
  <polygon class="top-wedge" points="357,0 666,0 666,25" fill="var(--band-gray)"/>
  <text class="sign-text tagline" x="27" y="46">PROVIDING THE BEST SERVICE TO YOUR HOME</text>
  <text class="sign-text tagline" x="27" y="66">SO YOU CAN LIVE COMFORTABLY</text>

  <circle class="brand-dot" cx="454" cy="55" r="26" fill="var(--brand-orange)"/>
  <text class="sign-text brand-name" x="492" y="67">CORLANTA</text>

  <!-- header stripes -->
  <polygon class="stripe-gray" points="0,75 666,121 666,131 0,88" fill="var(--band-gray)"/>
  <polygon class="stripe-green" points="0,91 666,133 666,147 0,122" fill="var(--brand-green)"/>
  <polygon class="stripe-orange" points="0,125 666,149 666,154 0,141" fill="var(--brand-orange)"/>

  <!-- photo area -->
  <g role="img" aria-label="Photo of a large Mediterranean-style home with palm trees, flower beds and a paver driveway on a sunny day">
    <polygon class="home-photo" points="0,143 666,154 666,400 0,363" fill="url(#photo-tones)"/>
  </g>

  <!-- footer stripes -->
  <polygon class="stripe-orange" points="0,363 666,400 666,408 0,379" fill="var(--brand-orange)"/>
  <polygon class="stripe-green" points="0,379 666,408 666,413 0,384" fill="var(--brand-green)"/>

  <!-- contact -->
  <path class="icon phone-icon" d="M24.5,403.5c1.2-1.2 2.4-1.1 3.2,0l1.8,2.4c0.6,0.9 0.4,1.8-0.4,2.5l-1,0.9c0.8,1.9 2.3,3.6 4.2,4.5l0.9-1c0.7-0.8 1.7-0.9 2.5-0.3l2.3,1.8c1,0.8 1,2 0,3.1c-1.7,1.7-3.9,2-6.2,0.9c-3.6-1.7-6.6-4.8-8.2-8.5c-0.9-2.2-0.6-4.3 0.9-6.3z"/>
  <text class="sign-text phone" x="39" y="419">555 014 2378</text>
  <text class="sign-text website" x="42" y="436">WWW.CORLANTA-EXAMPLE.NET</text>

  <!-- camera icon -->
  <g class="camera-icon">
    <path class="icon" d="M551,418h5l2-3h8l2,3h5c1.1,0 2,0.9 2,2v12c0,1.1-0.9,2-2,2h-22c-1.1,0-2-0.9-2-2v-12c0-1.1 0.9-2 2-2z"/>
    <circle cx="562" cy="426" r="4.6" fill="var(--sign-white)"/>
    <circle class="icon" cx="562" cy="426" r="2.8"/>
  </g>

  <!-- share icon -->
  <g class="share-icon">
    <line class="icon-stroke" x1="593" y1="425" x2="605" y2="418"/>
    <line class="icon-stroke" x1="593" y1="425" x2="605" y2="432"/>
    <circle class="icon" cx="592" cy="425" r="4"/>
    <circle class="icon" cx="606" cy="417" r="4"/>
    <circle class="icon" cx="606" cy="433" r="4"/>
  </g>
</svg>
</body>
</html>
```